Internal Web Pages for Metrivane Labs

I need internal web pages (Why Metrivane Labs?, What We Offer, Blog, Testimonials) that match the design of the homepage. These do not need to be as long or in-depth as the landing page (provided for reference) but I will need three, maybe four, total pages (I'll select the max number of pages for now, but these will all be simple and short pages). Also attached is our new logo design for the company.

They are to essentially be:
Why Metrivane Labs? - An About Us and Why Choose Us page rolled into one.
What We Offer - A Services type page
Blog - self-explanatory
Testimonials - Customer Reviews and Use Cases

Also, maybe a very simple "Contact Us" page as well.

Target Market(s)

Business professionals that work with data analytics teams

Industry/Entity Type

Data Science

Number of Pages Required

5+ page

Requirements
Must have
• It must match the original design in theme and colors.
Nice to have
• Simple pages that show continuity that flows from the original landing page.
Should not have
• Can not be a different design that does not match the landing page.

```html
<!DOCTYPE html>
<html lang="en">
<head>
<meta charset="utf-8">
<title>Blog – Metrivane Labs</title>
<link rel="stylesheet" href="https://fonts.googleapis.com/css2?family=Poppins:wght@300;400;500;600;700&display=swap">
<style>
:root{
  --ink:#1b1b2b;
  --muted:#4a4a58;
  --brand:#3a35d8;
  --brand-dark:#2a25b8;
  --orange:#f26a10;
  --page:#f4f2f5;
  --card:#ffffff;
  --footer:#1d0c47;
  --footer-deep:#160838;
  --line:#c9c9d2;
}
*{box-sizing:border-box;margin:0;padding:0}
html,body{width:1200px;height:4438px;overflow:hidden}
body{font-family:"Poppins",sans-serif;background:var(--page);color:var(--ink);position:relative}

.site-header{position:absolute;top:0;left:0;width:1200px;height:105px;background:#fff}
.brand{position:absolute;display:flex;align-items:center;gap:10px;font-weight:400;font-size:34px;color:var(--brand);letter-spacing:.2px}
.brand-mark{width:22px;height:22px;background:var(--brand)}
.site-header .brand{left:141px;top:30px}
.nav{position:absolute;left:475px;top:42px;display:flex;gap:0;font-size:16px;color:#333}
.nav a{color:inherit;text-decoration:none;position:absolute;white-space:nowrap}
.nav a.active{color:var(--brand)}
.cta{position:absolute;left:943px;top:38px;width:123px;height:33px;background:var(--orange);color:#fff;font-size:11.5px;font-weight:600;letter-spacing:.6px;display:flex;align-items:center;justify-content:center;box-shadow:0 3px 6px rgba(0,0,0,.2)}

.hero-edge{position:absolute;top:105px;left:0;width:1200px;height:520px;background:var(--brand);clip-path:polygon(0 0,100% 0,100% 390px,413px 508px,0 400px)}
.hero{position:absolute;top:105px;left:0;width:1200px;height:506px;background:#000;clip-path:polygon(0 0,100% 0,100% 386px,413px 500px,0 394px);overflow:hidden}
.hero-photo{position:absolute;left:465px;top:0;width:735px;height:506px;background:radial-gradient(circle at 45% 55%,#3fb6ff 0%,#1a5c9c 22%,#0d2a4e 48%,#07142a 72%,#000 100%)}
.hero-title{position:absolute;left:146px;top:272px;font-size:46px;font-weight:400;color:#fff;letter-spacing:1px}

.section-title{position:absolute;top:676px;left:0;width:1200px;text-align:center;font-size:29px;font-weight:400;color:var(--ink)}
.section-rule{position:absolute;top:731px;left:571px;width:58px;height:2px;background:#9a9aa6}

.field{position:absolute;top:787px;height:55px;border:1px solid #8d8d98;border-radius:6px;background:#fff;font-size:14px;color:#333;display:flex;align-items:center;padding:0 22px}
.field-search{left:133px;width:545px}
.field-filter{left:708px;width:361px}
.field svg{position:absolute;right:16px}
.filter-sep{position:absolute;right:46px;top:14px;width:1px;height:26px;background:#999}

.blog-grid{position:absolute;top:902px;left:133px;width:934px;display:grid;grid-template-columns:294px 294px 294px;column-gap:26px;row-gap:29px}
.post{height:456px;background:var(--card);box-shadow:0 2px 8px rgba(0,0,0,.07);position:relative}
.post-photo{height:174px}
.post-date{position:absolute;left:28px;top:199px;font-size:11px;font-weight:600;color:var(--ink)}
.post-title{position:absolute;left:28px;top:226px;width:246px;font-size:14px;font-weight:600;line-height:20px;color:var(--ink)}
.post-text{position:absolute;left:28px;top:283px;width:244px;font-size:12px;line-height:19.5px;color:var(--muted)}
.post-btn{position:absolute;left:32px;top:396px;width:79px;height:25px;background:var(--brand);border-radius:3px;color:#fff;font-size:10px;font-weight:600;display:flex;align-items:center;justify-content:center}

.ph-1{background:linear-gradient(135deg,#e6e8ee,#9fa8b8 60%,#d9dbe2)}
.ph-2{background:linear-gradient(160deg,#0d2a55,#1e5b9e 50%,#0b1d3b)}
.ph-3{background:radial-gradient(circle at 50% 60%,#5a56ff,#1b1a8c 55%,#0a0a3a)}
.ph-4{background:linear-gradient(135deg,#5d4b3e,#a9a6ad 45%,#e9e7e8)}
.ph-5{background:linear-gradient(135deg,#1c1c1c,#5b5f66 50%,#d7d9dc)}
.ph-6{background:radial-gradient(circle at 50% 60%,#4e7fbf,#1d2d4f 60%,#0e1528)}
.ph-7{background:linear-gradient(135deg,#3c2b22,#8a6a58 45%,#2a2a3a)}
.ph-8{background:linear-gradient(135deg,#d7e6f0,#9dbcd0 50%,#eef4f8)}
.ph-9{background:linear-gradient(135deg,#b9a796,#8fa0b8 50%,#c9b6a2)}
.ph-10{background:linear-gradient(135deg,#f2f4f8,#c4ccdf 50%,#eef0f5)}
.ph-11{background:linear-gradient(135deg,#f0786c,#f39a82 50%,#f06b5e)}
.ph-12{background:linear-gradient(135deg,#2a2a2e,#6b7794 55%,#c9d2e4)}
.ph-13{background:linear-gradient(135deg,#3d2fd6,#8f7ef0 45%,#e6e3ff)}
.ph-14{background:linear-gradient(160deg,#0e2f5e,#2e6fb3 50%,#0b2447)}
.ph-15{background:linear-gradient(135deg,#4a4a4a,#b6b8bd 50%,#e3e4e6)}
.ph-16{background:linear-gradient(135deg,#3f3b35,#8a8d7d 45%,#e2ddd3)}
.ph-17{background:linear-gradient(160deg,#04121f,#12557d 50%,#07253e)}
.ph-18{background:radial-gradient(circle at 50% 55%,#6b86ff,#1b2fa5 55%,#0a1454)}

.view-more{position:absolute;left:517px;top:3843px;width:161px;height:41px;border:2px solid var(--brand);border-radius:3px;background:#fff;color:var(--brand);font-size:14px;font-weight:600;display:flex;align-items:center;justify-content:center}

.site-footer{position:absolute;top:3939px;left:0;width:1200px;height:499px;background:linear-gradient(180deg,var(--footer),var(--footer-deep));color:#fff}
.site-footer .brand{left:141px;top:42px;color:#fff}
.site-footer .brand-mark{background:#fff}
.footer-about{position:absolute;left:143px;top:118px;width:288px;font-size:14px;line-height:22.5px;color:#e4e2f0}
.socials{position:absolute;left:146px;top:241px;display:flex;gap:9px}
.socials span{width:33px;height:33px;border:1.5px solid #fff;border-radius:50%}
.footer-heading{position:absolute;top:52px;font-size:17px;font-weight:600;letter-spacing:.4px;color:#fff}
.contact-list{position:absolute;left:479px;top:98px;width:240px;font-size:14.5px;line-height:21px;letter-spacing:.6px}
.contact-item{position:absolute;left:0;display:flex;gap:18px}
.contact-item svg{flex:none;margin-top:2px}
.newsletter-text{position:absolute;left:753px;top:96px;width:300px;font-size:13px;line-height:22px;color:#dcd9ec}
.newsletter-input{position:absolute;left:753px;top:162px;width:302px;height:36px;background:#fff;border-radius:2px;color:#555;font-size:13px;display:flex;align-items:center;padding-left:17px}
.newsletter-btn{position:absolute;left:753px;top:216px;width:127px;height:39px;background:var(--orange);color:#fff;font-size:13px;font-weight:600;display:flex;align-items:center;justify-content:center}
.copyright{position:absolute;left:0;top:440px;width:1200px;text-align:center;font-size:14.5px;color:#fff}
</style>
</head>
<body>

<header class="site-header">
  <div class="brand"><span class="brand-mark"></span>Metrivane Labs</div>
  <nav class="nav">
    <a class="active" style="left:0">Home</a>
    <a style="left:77px">About us</a>
    <a style="left:176px">Our Service</a>
    <a style="left:295px">Blog</a>
    <a style="left:358px">Contact</a>
  </nav>
  <div class="cta">GET STARTED</div>
</header>

<div class="hero-edge"></div>
<section class="hero">
  <div class="hero-photo" role="img" aria-label="Hand touching a glowing tablet with holographic growth charts"></div>
  <h1 class="hero-title">BLOG</h1>
</section>

<h2 class="section-title">LATEST BLOG</h2>
<div class="section-rule"></div>

<div class="field field-search">Search
  <svg width="14" height="14" viewBox="0 0 14 14"><circle cx="6" cy="6" r="4.5" fill="none" stroke="#333" stroke-width="1.6"/><line x1="9.3" y1="9.3" x2="13" y2="13" stroke="#333" stroke-width="1.8"/></svg>
</div>
<div class="field field-filter">Filter by
  <span class="filter-sep"></span>
  <svg width="12" height="8" viewBox="0 0 12 8"><path d="M1 1h10L6 7z" fill="#333"/></svg>
</div>

<main class="blog-grid">
  <article class="post"><div class="post-photo ph-1" role="img" aria-label="Laptop showing analytics dashboard"></div><p class="post-date">15 JUNE, 2021</p><h3 class="post-title">Lorem Ipsum is simply dummy text of the printing</h3><p class="post-text">There are many variations of passa ges of Lorem Ipsum available, but the majority have suffered alteration in some form, by injected humour, or randomised words.</p><span class="post-btn">Read More</span></article>
  <article class="post"><div class="post-photo ph-2" role="img" aria-label="Person facing a wall of data screens"></div><p class="post-date">15 JUNE, 2021</p><h3 class="post-title">Sed ut perspiciatis unde omnis iste natus error sit voluptat</h3><p class="post-text">Ut enim ad minima veniam, quis nos trum exercitationem ullam corporis suscipit laboriosam, nisi ut aliquid ex ea commodi consequaturQuis autem vel eum iure reprehenderit .</p><span class="post-btn">Read More</span></article>
  <article class="post"><div class="post-photo ph-3" role="img" aria-label="Glowing laptop with data graphics"></div><p class="post-date">15 JUNE, 2021</p><h3 class="post-title">At vero eos et accusamus et iust odio dignissimos duc</h3><p class="post-text">To take a trivial example, which of us ever undertakes laborious physical exercise, except to obtain some advantage from it? But who has any right to find fault with a man.</p><span class="post-btn">Read More</span></article>

  <article class="post"><div class="post-photo ph-4" role="img" aria-label="Tablet showing charts on a desk"></div><p class="post-date">15 JUNE, 2021</p><h3 class="post-title">These cases are perfectly simple and easy to distinguish</h3><p class="post-text">There are many variations of passa ges of Lorem Ipsum available, but the majority have suffered alteration in some form, by injected humour, or randomised words.</p><span class="post-btn">Read More</span></article>
  <article class="post"><div class="post-photo ph-5" role="img" aria-label="Team reviewing a monitor with graphs"></div><p class="post-date">15 JUNE, 2021</p><h3 class="post-title">But in certain circumstances and owing to the claims</h3><p class="post-text">Ut enim ad minima veniam, quis nos trum exercitationem ullam corporis suscipit laboriosam, nisi ut aliquid ex ea commodi consequaturQuis autem vel eum iure reprehenderit .</p><span class="post-btn">Read More</span></article>
  <article class="post"><div class="post-photo ph-6" role="img" aria-label="Hands holding a glowing data cloud"></div><p class="post-date">15 JUNE, 2021</p><h3 class="post-title">At vero eos et accusamus et iust odio dignissimos duc</h3><p class="post-text">To take a trivial example, which of us ever undertakes laborious physical exercise, except to obtain some advantage from it? But who has any right to find fault with a man.</p><span class="post-btn">Read More</span></article>

  <article class="post"><div class="post-photo ph-7" role="img" aria-label="Hands typing on a laptop keyboard"></div><p class="post-date">15 JUNE, 2021</p><h3 class="post-title">Nemo enim ipsam voluptatem quia voluptas sit aspernat</h3><p class="post-text">There are many variations of passa ges of Lorem Ipsum available, but the majority have suffered alteration in some form, by injected humour, or randomised words.</p><span class="post-btn">Read More</span></article>
  <article class="post"><div class="post-photo ph-8" role="img" aria-label="Person before a network of data icons"></div><p class="post-date">15 JUNE, 2021</p><h3 class="post-title">Nor again is there anyone who loves or pursues or desires</h3><p class="post-text">Ut enim ad minima veniam, quis nos trum exercitationem ullam corporis suscipit laboriosam, nisi ut aliquid ex ea commodi consequaturQuis autem vel eum iure reprehenderit .</p><span class="post-btn">Read More</span></article>
  <article class="post"><div class="post-photo ph-9" role="img" aria-label="Hands holding a tablet with charts"></div><p class="post-date">15 JUNE, 2021</p><h3 class="post-title">At vero eos et accusamus et iust odio dignissimos duc</h3><p class="post-text">To take a trivial example, which of us ever undertakes laborious physical exercise, except to obtain some advantage from it? But who has any right to find fault with a man.</p><span class="post-btn">Read More</span></article>

  <article class="post"><div class="post-photo ph-10" role="img" aria-label="Tablet with bar charts over printed reports"></div><p class="post-date">15 JUNE, 2021</p><h3 class="post-title">Lorem Ipsum is simply dummy text of the printing</h3><p class="post-text">There are many variations of passa ges of Lorem Ipsum available, but the majority have suffered alteration in some form, by injected humour, or randomised words.</p><span class="post-btn">Read More</span></article>
  <article class="post"><div class="post-photo ph-11" role="img" aria-label="Illustration of website data with magnifier"></div><p class="post-date">15 JUNE, 2021</p><h3 class="post-title">Sed ut perspiciatis unde omnis iste natus error sit voluptat</h3><p class="post-text">Ut enim ad minima veniam, quis nos trum exercitationem ullam corporis suscipit laboriosam, nisi ut aliquid ex ea commodi consequaturQuis autem vel eum iure reprehenderit .</p><span class="post-btn">Read More</span></article>
  <article class="post"><div class="post-photo ph-12" role="img" aria-label="Pen pointing at a dashboard screen"></div><p class="post-date">15 JUNE, 2021</p><h3 class="post-title">At vero eos et accusamus et iust odio dignissimos duc</h3><p class="post-text">To take a trivial example, which of us ever undertakes laborious physical exercise, except to obtain some advantage from it? But who has any right to find fault with a man.</p><span class="post-btn">Read More</span></article>

  <article class="post"><div class="post-photo ph-13" role="img" aria-label="Figure with a holographic city display"></div><p class="post-date">15 JUNE, 2021</p><h3 class="post-title">Lorem Ipsum is simply dummy text of the printing</h3><p class="post-text">There are many variations of passa ges of Lorem Ipsum available, but the majority have suffered alteration in some form, by injected humour, or randomised words.</p><span class="post-btn">Read More</span></article>
  <article class="post"><div class="post-photo ph-14" role="img" aria-label="Analyst surrounded by data overlays"></div><p class="post-date">15 JUNE, 2021</p><h3 class="post-title">Sed ut perspiciatis unde omnis iste natus error sit voluptat</h3><p class="post-text">Ut enim ad minima veniam, quis nos trum exercitationem ullam corporis suscipit laboriosam, nisi ut aliquid ex ea commodi consequaturQuis autem vel eum iure reprehenderit .</p><span class="post-btn">Read More</span></article>
  <article class="post"><div class="post-photo ph-15" role="img" aria-label="Tablet with charts beside a coffee cup"></div><p class="post-date">15 JUNE, 2021</p><h3 class="post-title">At vero eos et accusamus et iust odio dignissimos duc</h3><p class="post-text">To take a trivial example, which of us ever undertakes laborious physical exercise, except to obtain some advantage from it? But who has any right to find fault with a man.</p><span class="post-btn">Read More</span></article>

  <article class="post"><div class="post-photo ph-16" role="img" aria-label="Laptop on a desk with plants"></div><p class="post-date">15 JUNE, 2021</p><h3 class="post-title">Lorem Ipsum is simply dummy text of the printing</h3><p class="post-text">There are many variations of passa ges of Lorem Ipsum available, but the majority have suffered alteration in some form, by injected humour, or randomised words.</p><span class="post-btn">Read More</span></article>
  <article class="post"><div class="post-photo ph-17" role="img" aria-label="Hands on keyboard under glowing charts"></div><p class="post-date">15 JUNE, 2021</p><h3 class="post-title">Sed ut perspiciatis unde omnis iste natus error sit voluptat</h3><p class="post-text">Ut enim ad minima veniam, quis nos trum exercitationem ullam corporis suscipit laboriosam, nisi ut aliquid ex ea commodi consequaturQuis autem vel eum iure reprehenderit .</p><span class="post-btn">Read More</span></article>
  <article class="post"><div class="post-photo ph-18" role="img" aria-label="Glowing laptop with floating data panels"></div><p class="post-date">15 JUNE, 2021</p><h3 class="post-title">At vero eos et accusamus et iust odio dignissimos duc</h3><p class="post-text">To take a trivial example, which of us ever undertakes laborious physical exercise, except to obtain some advantage from it? But who has any right to find fault with a man.</p><span class="post-btn">Read More</span></article>
</main>

<div class="view-more">View more Blogs</div>

<footer class="site-footer">
  <div class="brand"><span class="brand-mark"></span>Metrivane Labs</div>
  <p class="footer-about">Sed ut perspiciatis unde omnis iste natus error sit voluptatem accusantium dolorque laudantium, totam rem aperiam, eaque ipsa quae ab illo inventore veritatis et quasi</p>
  <div class="socials"><span></span><span></span><span></span><span></span></div>

  <h4 class="footer-heading" style="left:479px">CONTACT US</h4>
  <div class="contact-list">
    <div class="contact-item" style="top:0">
      <svg width="20" height="24" viewBox="0 0 20 24"><path d="M10 23s8-8 8-14a8 8 0 0 0-16 0c0 6 8 14 8 14z" fill="none" stroke="#fff" stroke-width="1.5"/><circle cx="10" cy="9" r="3" fill="none" stroke="#fff" stroke-width="1.5"/></svg>
      <div>Metrivane Labs<br>250 ipsam voluptatem<br>quia voluptas</div>
    </div>
    <div class="contact-item" style="top:82px">
      <svg width="20" height="20" viewBox="0 0 20 20"><path d="M4 1l4 4-2 3c1 3 3 5 6 6l3-2 4 4-3 3C8 19 1 12 1 4z" fill="none" stroke="#fff" stroke-width="1.4"/></svg>
      <div>Phone :<br>555-0142-7788</div>
    </div>
    <div class="contact-item" style="top:146px">
      <svg width="20" height="16" viewBox="0 0 20 16"><rect x="1" y="1" width="18" height="14" fill="none" stroke="#fff" stroke-width="1.4"/><path d="M1 1l9 8 9-8" fill="none" stroke="#fff" stroke-width="1.4"/></svg>
      <div>Email :<br>hello@metrivanelabs.com</div>
    </div>
  </div>

  <h4 class="footer-heading" style="left:753px">STAY UP TO DATE WITH METRIVANE LABS</h4>
  <p class="newsletter-text">Excepteur sint occaecat cupidatat non proi- dent, sunt in culpa qui Nemo enim ipsam vo-</p>
  <div class="newsletter-input">Enter Email</div>
  <div class="newsletter-btn">SUBSCRIBE</div>

  <p class="copyright">Copyright © Metrivane Labs 2021. All rights reserved. | Privacy Policy</p>
</footer>

</body>
</html>
```